Pool service company wants new Wix website design

I want a multi-page website including:
Home
About Us
Services Offered
Contact
Products page
Blog
Target Market(s)
Swimming pool owners. Residential only.
Industry/Entity Type
Swimming pool care, service, maintenance and repair.
Other font styles liked:
- Arial, Calibre
Requirements
Must have
- Wix compatible.

```html
<!DOCTYPE html>
<html lang="en">
<head>
<meta charset="utf-8">
<title>Clearwell Pools – Pool &amp; Spa Service</title>
<link href="https://fonts.googleapis.com/css2?family=Arimo:wght@400;700&family=Lato:wght@400;700&display=swap" rel="stylesheet">
<style>
:root{
  --red:#e63a1f;
  --navy:#0c3563;
  --navy-band:#0a3766;
  --ink:#1b2b48;
  --grey:#8a8a8a;
  --footer:#2d2d2d;
  --footer-base:#232323;
  --white:#ffffff;
}
*{box-sizing:border-box;margin:0;padding:0}
html,body{width:1200px;height:2815px;overflow:hidden;background:var(--white)}
body{position:relative;font-family:"Arimo",Arial,sans-serif;color:var(--ink)}
.abs{position:absolute}

/* header */
.site-header{left:0;top:0;width:1200px;height:96px;background:var(--white);z-index:3}
.brand-block{left:38px;top:0;width:304px;height:158px;background:var(--red);border-radius:0 0 26px 26px;z-index:4;display:flex;align-items:center;justify-content:center}
.brand-name{font-family:"Arimo",Arial,sans-serif;font-weight:700;font-size:34px;color:var(--white);letter-spacing:1px}
.nav a{position:absolute;top:34px;font-size:19px;color:var(--navy);text-decoration:none;font-family:"Lato",sans-serif}
.nav a.current{color:var(--red)}

/* hero */
.hero-photo{left:0;top:88px;width:1200px;height:583px;background:linear-gradient(120deg,#4a86a6 0%,#2f6f95 35%,#1f5a84 65%,#5d7390 100%)}
.hero-shade{left:560px;top:88px;width:596px;height:583px;background:rgba(10,40,70,.35)}
.hero-title{left:632px;top:258px;width:520px;font-size:48px;font-weight:700;line-height:47px;color:var(--white)}
.hero-sub{left:633px;top:370px;width:420px;font-family:"Lato",sans-serif;font-size:17px;line-height:22px;color:#e6eef5}
.btn-request{left:632px;top:434px;width:225px;height:40px;background:var(--red);color:var(--white);font-family:"Lato",sans-serif;font-size:17px;display:flex;align-items:center;justify-content:center}

/* about */
.about-photo{left:0;top:699px;width:578px;height:324px;background:linear-gradient(135deg,#2c6fae,#4c8fc7 55%,#c9cdd2 80%)}
.about-title{left:654px;top:768px;font-size:39px;font-weight:700;color:var(--red)}
.about-tagline{left:654px;top:808px;font-size:21px;font-weight:700;color:var(--red)}
.about-text{left:654px;top:874px;width:485px;font-size:20px;line-height:17.5px;color:var(--grey)}

/* services */
.services{left:2px;top:1056px;width:1193px;height:584px;background:var(--navy-band)}
.services-title{left:0;top:1088px;width:1200px;text-align:center;font-size:39px;font-weight:700;color:var(--white)}
.service{position:absolute;top:1186px;width:260px}
.service-photo{width:185px;height:185px;border-radius:50%;margin:0 auto}
.service h3{text-align:center;font-size:26px;font-weight:700;color:var(--white);margin-top:20px}
.service p{font-size:18.5px;line-height:22px;color:#b6c2d3;margin-top:20px;padding-left:7px}
.service a{display:inline-block;margin-top:12px;margin-left:9px;font-size:18.5px;color:var(--white);text-decoration:underline}
.service a::after{content:"";display:inline-block;width:7px;height:7px;border-radius:50%;background:var(--red);margin-left:8px;vertical-align:middle}

/* why */
.why-title{left:96px;top:1724px;font-size:39px;font-weight:700;color:var(--red)}
.why-tagline{left:96px;top:1767px;font-size:21px;font-weight:700;color:var(--red)}
.why-list{left:100px;top:1817px;list-style:none}
.why-list li{display:flex;align-items:center;height:29.5px;font-family:"Lato",sans-serif;font-size:16.5px;color:var(--grey)}
.why-list svg{margin-right:9px}
.why-photo{left:620px;top:1680px;width:578px;height:323px;background:linear-gradient(135deg,#c9b79c,#5f8fa8 45%,#2d78b0 75%,#1f4f8a)}

/* contact */
.band-left{left:4px;top:2121px;width:582px;height:54px;background:var(--red)}
.band-right{left:1000px;top:2121px;width:196px;height:54px;background:var(--red)}
.mascot{left:27px;top:2011px;width:483px;height:531px;background:linear-gradient(180deg,#e1783a 0%,#2a66b0 45%,#e1783a 75%,#2a66b0 100%);opacity:.85;border-radius:40px}
.contact-title{left:622px;top:2116px;font-size:48px;font-weight:700;line-height:37px;color:var(--navy)}
.contact-sub{left:620px;top:2229px;font-size:19.5px;font-weight:700;line-height:20px;color:var(--navy)}
.field{position:absolute;border-bottom:2.5px solid var(--navy);font-size:9.5px;color:var(--navy);height:24px}
.btn-send{left:617px;top:2454px;width:333px;height:31px;background:var(--red);color:var(--white);font-size:10px;display:flex;align-items:center;justify-content:center}

/* footer */
.footer{left:0;top:2558px;width:1200px;height:202px;background:var(--footer)}
.footer-base{left:0;top:2760px;width:1200px;height:55px;background:var(--footer-base);border-top:1px solid #444}
.footer-brand{left:98px;top:2642px;font-size:30px;font-weight:700;color:var(--white)}
.foot-col h4{font-size:14px;font-weight:700;color:var(--white);letter-spacing:.5px}
.foot-col p{font-size:9px;line-height:15px;color:#d0d0d0}
.contact-line{display:flex;gap:6px}
.contact-line svg{flex:none;margin-top:3px}
.news-input{left:826px;top:2677px;width:191px;height:22px;background:var(--white);font-size:9px;color:#999;padding:5px 6px}
.news-btn{left:1017px;top:2677px;width:63px;height:22px;background:var(--red);color:var(--white);font-size:9px;font-weight:700;display:flex;align-items:center;justify-content:center}
.social{top:2715px;width:22px;height:22px;background:var(--white);border-radius:3px}
.copyright{left:0;top:2783px;width:1200px;text-align:center;font-size:8.5px;color:#8c8c8c}
</style>
</head>
<body>

<header class="abs site-header">
  <nav class="nav">
    <a style="left:563px">About us</a>
    <a style="left:697px">Services</a>
    <a style="left:825px">Products</a>
    <a style="left:959px">Blog</a>
    <a class="current" style="left:1054px">Contact</a>
  </nav>
</header>
<div class="abs brand-block"><span class="brand-name">Clearwell Pools</span></div>

<section>
  <div class="abs hero-photo" role="img" aria-label="Aerial view of a blue pool with sun loungers and a spa"></div>
  <div class="abs hero-shade"></div>
  <h1 class="abs hero-title">We clean, repair and maintain.</h1>
  <p class="abs hero-sub">Exceptional pool service that our clients trust at affordable prices!</p>
  <div class="abs btn-request">Request Service</div>
</section>

<section>
  <div class="abs about-photo" role="img" aria-label="Technician skimming a pool with a leaf net"></div>
  <h2 class="abs about-title">Clearwell Pools Pool Service</h2>
  <p class="abs about-tagline">Pool Care, Cleaning &amp; Equipment Repair</p>
  <p class="abs about-text">Welcome to Clearwell Pools, a family of pool owners who, just like you, have come to rely and enjoy the benefits of having a happy, healthy pool year-round without the stress and worry.</p>
</section>

<section>
  <div class="abs services"></div>
  <h2 class="abs services-title">Our Services</h2>
  <div class="service" style="left:167px">
    <div class="service-photo" role="img" aria-label="Pool vacuum head cleaning the pool floor" style="background:radial-gradient(circle at 40% 40%,#bfe0f2,#4f9bd3 60%,#1f5fb8)"></div>
    <h3>Pool Cleaning</h3>
    <p>Lorem ipsum dolor sit<br>amet, consectetur<br>adipiscing elit, sed do</p>
    <a>Learn more</a>
  </div>
  <div class="service" style="left:474px">
    <div class="service-photo" role="img" aria-label="Automatic pool cleaner under water" style="background:radial-gradient(circle at 50% 50%,#e8eef4,#5fb3d8 50%,#2f8fc0)"></div>
    <h3>Pool Inspection</h3>
    <p>Lorem ipsum dolor sit<br>amet, consectetur<br>adipiscing elit, sed do</p>
    <a>Learn more</a>
  </div>
  <div class="service" style="left:773px">
    <div class="service-photo" role="img" aria-label="Technician repairing an empty pool wall" style="background:linear-gradient(180deg,#d9c7b0,#f2f2f2 45%,#7b8b9c)"></div>
    <h3>Pool Repair</h3>
    <p>Lorem ipsum dolor sit<br>amet, consectetur<br>adipiscing elit, sed do</p>
    <a>Learn more</a>
  </div>
</section>

<section>
  <h2 class="abs why-title">Why Choose Us:</h2>
  <p class="abs why-tagline">With more than 35 years experience</p>
  <ul class="abs why-list">
    <li><svg width="21" height="21" viewBox="0 0 21 21"><circle cx="10.5" cy="10.5" r="8" fill="none" stroke="var(--red)" stroke-width="4"/><circle cx="10.5" cy="10.5" r="8" fill="none" stroke="var(--navy)" stroke-width="4" stroke-dasharray="4 8.6"/></svg>Pet friendly</li>
    <li><svg width="21" height="21" viewBox="0 0 21 21"><circle cx="10.5" cy="10.5" r="8" fill="none" stroke="var(--red)" stroke-width="4"/><circle cx="10.5" cy="10.5" r="8" fill="none" stroke="var(--navy)" stroke-width="4" stroke-dasharray="4 8.6"/></svg>5-star customer reviews</li>
    <li><svg width="21" height="21" viewBox="0 0 21 21"><circle cx="10.5" cy="10.5" r="8" fill="none" stroke="var(--red)" stroke-width="4"/><circle cx="10.5" cy="10.5" r="8" fill="none" stroke="var(--navy)" stroke-width="4" stroke-dasharray="4 8.6"/></svg>Friendly, uniformed pool technicians</li>
    <li><svg width="21" height="21" viewBox="0 0 21 21"><circle cx="10.5" cy="10.5" r="8" fill="none" stroke="var(--red)" stroke-width="4"/><circle cx="10.5" cy="10.5" r="8" fill="none" stroke="var(--navy)" stroke-width="4" stroke-dasharray="4 8.6"/></svg>Same day, same service person</li>
    <li><svg width="21" height="21" viewBox="0 0 21 21"><circle cx="10.5" cy="10.5" r="8" fill="none" stroke="var(--red)" stroke-width="4"/><circle cx="10.5" cy="10.5" r="8" fill="none" stroke="var(--navy)" stroke-width="4" stroke-dasharray="4 8.6"/></svg>Fully insured for your protection</li>
  </ul>
  <div class="abs why-photo" role="img" aria-label="Blue pool vacuum head and hose lifted out of the water"></div>
</section>

<section>
  <div class="abs band-left"></div>
  <div class="abs band-right"></div>
  <div class="abs mascot" role="img" aria-label="Illustrated pool technician holding a leaf net over his shoulder"></div>
  <h2 class="abs contact-title">We are ready to<br>serve you!</h2>
  <p class="abs contact-sub">Contact us to request our services or<br>for more information about out services</p>
  <div class="field" style="left:619px;top:2307px;width:156px">First Name</div>
  <div class="field" style="left:792px;top:2307px;width:157px">Last Name</div>
  <div class="field" style="left:619px;top:2361px;width:156px">Email</div>
  <div class="field" style="left:792px;top:2361px;width:157px">Address</div>
  <div class="field" style="left:619px;top:2408px;width:329px;height:36px">Leave a message...</div>
  <div class="abs btn-send">Send</div>
</section>

<footer>
  <div class="abs footer"></div>
  <div class="abs footer-brand">Clearwell Pools</div>
  <div class="abs foot-col" style="left:444px;top:2618px">
    <h4>SUPPORT</h4>
    <p style="margin-top:4px">Contact us<br>FAQ<br>Payments<br>Terms &amp; Conditions<br>Privacy Policy</p>
  </div>
  <div class="abs foot-col" style="left:579px;top:2618px;width:200px">
    <h4>CONTACT</h4>
    <div style="margin-top:4px">
      <div class="contact-line"><svg width="8" height="9" viewBox="0 0 8 9"><path d="M4 0a3 3 0 0 1 3 3c0 2-3 6-3 6S1 5 1 3a3 3 0 0 1 3-3z" fill="var(--red)"/></svg><p>Lorem ipsum dolor sit amet, consectetur<br>adipiscing elit.</p></div>
      <div class="contact-line"><svg width="8" height="9" viewBox="0 0 8 9"><rect x="2" y="0.5" width="4" height="8" rx="1" fill="none" stroke="var(--red)"/></svg><p>(555) 014-2290</p></div>
      <div class="contact-line"><svg width="8" height="9" viewBox="0 0 8 9"><path d="M1 8l1-3 5-5 1 1-5 5z" fill="var(--red)"/></svg><p>info@clearwellpools.com</p></div>
      <div class="contact-line"><svg width="8" height="9" viewBox="0 0 8 9"><circle cx="4" cy="4.5" r="3.5" fill="var(--red)"/><path d="M4 2.5v2h1.5" stroke="#fff" fill="none" stroke-width=".8"/></svg><p>Mon - Fri: 8am - 4pm</p></div>
    </div>
  </div>
  <div class="abs foot-col" style="left:826px;top:2618px;width:260px">
    <h4>JOIN OUR NEWSLETTER</h4>
    <p style="margin-top:2px">Sign up hear more about special offers, blog posts, and new products.</p>
  </div>
  <div class="abs news-input">E-mail</div>
  <div class="abs news-btn">Sign Up</div>
  <div class="abs social" style="left:828px"></div>
  <div class="abs social" style="left:857px"></div>
  <div class="abs social" style="left:886px"></div>
  <div class="abs footer-base"></div>
  <p class="abs copyright">© 2022 Clearwell Pools. All rights reserved.</p>
</footer>

</body>
</html>
```